Game, Voice & Dedicated Server Company Needs a Business Card Design

We need a new business card design, centered around our new logo (PSD provided below).

Designs that we do like:
https://pixelmarsh.net/item/corporate-business-card/5382017?s_rank=43 (needs to be made more eye catching)

Our main areas of business are:
- Dedicated Servers
- Game Servers
- Voice Servers
- Mitigation Security Specialists

Industry/Entity Type

Business

Contact Information for Business Card

On the card: (and anything else you would suggest)
- Staff member name
- Staff member position in company
- Staff member phone number
- Staff member email
- Other / Staff member Skype
- Website link

Colors
9bcb3c
abd036

Requirements
Must have
• Design of Card:
• - Green (same green as the logo)
• - Business / Corporate design
• - Something a little different / abstract that shouts premium

```html
<!DOCTYPE html>
<html lang="en">
<head>
<meta charset="utf-8">
<title>Ridgeway Hosting – Business Card</title>
<link href="https://fonts.googleapis.com/css2?family=Archivo:wght@700&family=Questrial&display=swap" rel="stylesheet">
<style>
  :root {
    --green: #8dc63f;
    --slate: #6d6e70;
    --ink: #58595b;
    --paper: #ffffff;
    --backdrop: #ece7dd;
    --rule: #2b2b2b;
  }
  * { box-sizing: border-box; margin: 0; padding: 0; }
  html, body { width: 1189px; height: 1200px; overflow: hidden; }
  body { background: var(--backdrop); position: relative; font-family: "Questrial", sans-serif; }

  .card {
    position: absolute; left: 166px; width: 856px; height: 487px;
    border-radius: 22px; box-shadow: 4px 6px 10px rgba(0,0,0,.25);
  }
  .card--front { top: 68px; background: var(--slate); }
  .card--back { top: 627px; background: var(--paper); }

  .brand { display: flex; align-items: center; gap: 22px; }
  .brand__mark { width: 26px; height: 26px; background: var(--green); flex: none; }
  .brand__name {
    font-family: "Archivo", sans-serif; font-weight: 700; color: var(--green);
    letter-spacing: -2px; line-height: .95; text-transform: uppercase;
  }

  .card--front .brand { position: absolute; left: 190px; top: 180px; }
  .card--front .brand__name { font-size: 58px; }

  .services {
    position: absolute; left: 0; right: 0; top: 321px; text-align: center;
    color: #fff; font-size: 23px; line-height: 31px; letter-spacing: .3px;
  }
  .services__sep { color: var(--green); padding: 0 6px; }

  .card--back .brand {
    position: absolute; left: 62px; top: 232px; width: 300px;
    flex-direction: column; gap: 18px;
  }
  .card--back .brand__name { font-size: 48px; text-align: center; }

  .divider { position: absolute; left: 410px; top: 116px; width: 2px; height: 267px; background: var(--rule); }

  .person { position: absolute; left: 464px; top: 122px; }
  .person__name { font-family: "Archivo", sans-serif; font-weight: 700; font-size: 28px; color: var(--green); letter-spacing: .5px; line-height: 30px; }
  .person__role { font-size: 21px; color: var(--ink); line-height: 22px; }

  .contacts { position: absolute; left: 464px; top: 270px; list-style: none; }
  .contacts li { display: flex; align-items: center; gap: 7px; height: 26px; margin-bottom: 1px; font-size: 24px; color: var(--ink); }
  .contacts svg { width: 22px; height: 22px; flex: none; }
</style>
</head>
<body>
  <section class="card card--front">
    <div class="brand">
      <span class="brand__mark"></span>
      <span class="brand__name">Ridgeway<br>Hosting</span>
    </div>
    <p class="services">
      Dedicated Servers<span class="services__sep">|</span>Game Servers<span class="services__sep">|</span>Voice Servers<br>
      Business relations
    </p>
  </section>

  <section class="card card--back">
    <div class="brand">
      <span class="brand__mark"></span>
      <span class="brand__name">Ridgeway<br>Hosting</span>
    </div>
    <div class="divider"></div>
    <div class="person">
      <p class="person__name">ALAN REYES</p>
      <p class="person__role">Manager</p>
    </div>
    <ul class="contacts">
      <li>
        <svg viewBox="0 0 22 22"><rect width="22" height="22" rx="3" fill="#8dc63f"/><path d="M5 9c0-2 3-3 6-3s6 1 6 3l-2 1-1-2h-6l-1 2zM7 11h8l1 6H6z" fill="#fff"/></svg>
        555 018 2740
      </li>
      <li>
        <svg viewBox="0 0 22 22"><rect width="22" height="22" rx="3" fill="#8dc63f"/><rect x="4" y="6" width="14" height="10" fill="none" stroke="#fff" stroke-width="1.5"/><path d="M4 6l7 6 7-6M4 16l5-5M18 16l-5-5" fill="none" stroke="#fff" stroke-width="1.5"/></svg>
        alan@ridgewayhost.com
      </li>
      <li>
        <svg viewBox="0 0 22 22"><rect width="22" height="22" rx="3" fill="#8dc63f"/><circle cx="11" cy="11" r="7" fill="none" stroke="#fff" stroke-width="1.4"/><ellipse cx="11" cy="11" rx="3" ry="7" fill="none" stroke="#fff" stroke-width="1.2"/><path d="M4 11h14M5 7.5h12M5 14.5h12" stroke="#fff" stroke-width="1.2"/></svg>
        www.ridgewayhost.com
      </li>
      <li>
        <svg viewBox="0 0 22 22"><rect width="22" height="22" rx="3" fill="#8dc63f"/><circle cx="11" cy="11" r="6.5" fill="none" stroke="#fff" stroke-width="1.6"/><path d="M13 8.5c-1-1-4-1-4 .8s4 1.2 4 3.2-3 2-4 .8" fill="none" stroke="#fff" stroke-width="1.5"/></svg>
        alanreyes.rh
      </li>
    </ul>
  </section>
</body>
</html>
```